SunnyPawLand Webshop and Logo Design

We need a complete design for our new Webshop
We sell pet accessories for dogs, cats, guinea pigs and some other animals
The provided logo ist a first draft for our logo and not final. you can be creative.
Maybe you can bring in some "Happyness" :o)
The Website will be a PressKit/KartMill System with a "ShopCanvas" Theme. We can provide a test environment, but it must be transferable to the final website.
In the First step, we need a finalized logo, then the WebDesign.

We need the following items.

* Company Icon
* Favicon 512*512 (from company icon)
* Shipping Label Icon (300px*100px, transparent background)
* Label Icon (600px*150px, transparent background)
* WebShop Design/Child-Theme
* Businesscard

Target Market(s)

German retail for pet accessories

Industry/Entity Type

Pet

Logo Text

SunnyPawLand

Coding

Coded - Design and coding required

Number of Pages Required

3 page

Colors

Designer to choose colors to be used in the design.

Requirements
Must have
• Cat, Dog, and Guineapig must be present
• The design must communicate happy pets.

```html
<!DOCTYPE html>
<html lang="en">
<head>
<meta charset="utf-8">
<title>SunnyPawLand</title>
<link href="https://fonts.googleapis.com/css2?family=Montserrat:wght@400;500;600;700&family=Raleway:wght@400;500;600&display=swap" rel="stylesheet">
<style>
:root{
  --green:#7cb529;
  --blue:#0a6ab5;
  --blue-dark:#07589a;
  --text:#333;
  --grey-bg:#ececec;
  --border:#cfcfcf;
  --white:#fff;
}
*{margin:0;padding:0;box-sizing:border-box}
html,body{width:948px;height:1200px;overflow:hidden;background:var(--white)}
body{position:relative;font-family:"Raleway",sans-serif;color:var(--text)}
.abs{position:absolute}
.topbar{left:0;top:0;width:948px;height:20px;background:var(--green);color:var(--white);font-size:8px;line-height:20px}
.topbar .phone{position:absolute;left:59px}
.topbar .links{position:absolute;right:174px;display:flex;gap:20px}
.brand{display:flex;align-items:center;gap:6px;font-family:"Montserrat",sans-serif;font-weight:600;white-space:nowrap}
.brand-header{left:58px;top:68px;font-size:16px;color:var(--green)}
.brand-dot{width:22px;height:22px;border-radius:50%;background:var(--blue)}
.account{left:242px;top:52px;font-size:8px;color:var(--green)}
.cart{left:308px;top:49px;font-size:8px;color:var(--green);display:flex;align-items:center;gap:4px}
.cart b{font-family:"Montserrat",sans-serif;font-size:10.5px}
.search{left:232px;top:68px;width:354px;height:33px;border-radius:12px;background:var(--grey-bg);display:flex;align-items:center;padding-left:13px;gap:10px;font-size:8.5px;color:#888}
.search-btn{left:598px;top:68px;width:65px;height:33px;border-radius:10px;background:var(--green);color:var(--white);font-size:8.5px;text-align:center;line-height:33px}
.nav{left:58px;top:126px;display:flex;gap:21px;font-size:10px;color:var(--blue)}
.hero{left:0;top:152px;width:948px;height:194px;background:var(--blue);overflow:hidden}
.hero-arc{position:absolute;left:452px;top:42px;width:500px;height:420px;border-radius:50%;background:var(--blue-dark)}
.hero h1{position:absolute;left:61px;top:44px;font-family:"Montserrat",sans-serif;font-weight:500;font-size:22px;color:var(--white)}
.hero p{position:absolute;left:61px;top:78px;font-family:"Montserrat",sans-serif;font-weight:500;font-size:11px;line-height:13.5px;color:var(--white)}
.hero-btn{position:absolute;left:58px;top:126px;width:105px;height:28px;border-radius:14px;background:var(--green);color:var(--white);font-family:"Montserrat",sans-serif;font-weight:600;font-size:10.5px;text-align:center;line-height:28px}
.pet-cat{left:502px;top:158px;width:186px;height:258px;border-radius:70px 70px 40px 40px;background:linear-gradient(180deg,#8a8c94 0%,#9b9ca3 55%,#b8b9bf 85%,rgba(200,200,205,0) 100%)}
.pet-dog{left:688px;top:76px;width:200px;height:364px;border-radius:90px 90px 30px 30px;background:linear-gradient(180deg,#e3c99a 0%,#efdcbc 45%,#f3e6cf 85%,#ead8b8 100%)}
.side{left:709px;top:404px;width:173px;height:244px;border-radius:10px;background:var(--green)}
.side-inner{position:absolute;left:9px;top:44px;width:156px;height:192px;border-radius:10px;background:var(--white)}
.side-btn{position:absolute;left:5px;width:145px;height:29px;border-radius:10px;background:var(--green);color:var(--white);font-size:10.5px;text-align:center;line-height:29px}
.side-btn.active{background:var(--blue)}
.section-title{left:55px;top:386px;font-family:"Montserrat",sans-serif;font-weight:500;font-size:18px;color:var(--blue)}
.card{position:absolute;width:176px}
.card .photo{width:174px;height:173px;border:1px solid var(--border)}
.card h3{margin-top:7px;font-family:"Montserrat",sans-serif;font-weight:600;font-size:10.5px;color:var(--blue);white-space:nowrap}
.card .price{margin-top:2px;font-size:8px;font-weight:600;color:var(--green)}
.card .desc{margin-top:1px;font-size:7.5px;line-height:9.5px;color:var(--text)}
.footer{left:0;top:974px;width:948px;height:185px;background:var(--green);color:var(--white)}
.brand-footer{position:absolute;left:58px;top:50px;font-size:16px;color:var(--white)}
.brand-footer .brand-dot{background:var(--white)}
.footer-about{position:absolute;left:58px;top:102px;width:195px;font-size:7.5px;line-height:9.2px}
.footer h4{position:absolute;top:38px;font-family:"Montserrat",sans-serif;font-weight:500;font-size:11px}
.footer ul{position:absolute;top:63px;list-style:none;font-size:8px;line-height:14.4px}
.footer li::before{content:"";display:inline-block;width:0;height:0;border-left:4px solid var(--white);border-top:3px solid transparent;border-bottom:3px solid transparent;margin-right:8px}
.contact{position:absolute;left:642px;top:63px;font-size:8px;line-height:14.4px}
.contact div{display:flex;align-items:center;gap:9px}
.bottom{left:0;top:1159px;width:948px;height:41px;background:var(--blue);color:var(--white);font-size:7.5px}
.bottom .copy{position:absolute;left:60px;top:16px}
.social{position:absolute;right:80px;top:15px;display:flex;gap:6px}
.social span{width:9px;height:9px;border-radius:50%;background:var(--white)}
</style>
</head>
<body>
<div class="abs topbar">
  <span class="phone">+49 (800) 555-0142 Days a week from 9:00 am to 7:00 pm</span>
  <span class="links"><span>Orders</span><span>Compare</span><span>Wishlist</span><span>Log in</span></span>
</div>

<div class="abs brand brand-header"><span class="brand-dot"></span>SunnyPawLand</div>
<div class="abs account">My Account</div>
<div class="abs cart">
  <svg width="9" height="8" viewBox="0 0 9 8"><path d="M0 2h9L8 8H1z" fill="#7cb529"/><path d="M2 2L4 0M7 2L5 0" stroke="#7cb529" stroke-width="1"/></svg>
  <b>$0.00</b> 0 items
</div>
<div class="abs search">
  <svg width="14" height="14" viewBox="0 0 14 14"><circle cx="5.5" cy="5.5" r="4.3" fill="none" stroke="#555" stroke-width="1.8"/><path d="M8.7 8.7L13 13" stroke="#555" stroke-width="2"/></svg>
  search products
</div>
<div class="abs search-btn">search</div>
<nav class="abs nav"><span>Food &amp; Treats</span><span>Accessories</span><span>Cages &amp; Aquariums</span><span>Toys</span><span>Grooming</span></nav>

<section class="abs hero">
  <div class="hero-arc"></div>
  <h1>Welcome to SunnyPawLand</h1>
  <p>Here you'll find everything you need for your best furry friend.<br>Shop premium pet food, accessories, grooming supplies, and more!</p>
  <div class="hero-btn">SHOP NOW</div>
</section>

<aside class="abs side">
  <div class="side-inner">
    <div class="side-btn active" style="top:16px">Recent Products</div>
    <div class="side-btn" style="top:49px">Top Selling</div>
    <div class="side-btn" style="top:82px">On Sale</div>
    <div class="side-btn" style="top:115px">Foods &amp; Treats</div>
    <div class="side-btn" style="top:148px">Accessories</div>
  </div>
</aside>

<div class="abs pet-cat" role="img" aria-label="Grey cat peeking over the hero edge"></div>
<div class="abs pet-dog" role="img" aria-label="Golden puppy resting its paws on the product menu"></div>

<h2 class="abs section-title">Recent Products</h2>

<div class="card" style="left:56px;top:434px">
  <div class="photo" role="img" aria-label="Black dog chewing a rope toy" style="background:linear-gradient(#fff 30%,#3a3028 55%,#f2f2f2 80%)"></div>
  <h3>Chew Ropes</h3><div class="price">Price: $8.00</div>
  <div class="desc">Lorem ipsum dolor sit amet, consectetur adipiscing elit, sed do eiusmod tempor .</div>
</div>
<div class="card" style="left:269px;top:434px">
  <div class="photo" role="img" aria-label="Orange and pink travel food bowls" style="background:linear-gradient(#fff 25%,#f0893a 50%,#e5407a 65%,#fff 80%)"></div>
  <h3>On the Go Food and Water Bowl</h3><div class="price">Price: $8.00</div>
  <div class="desc">Lorem ipsum dolor sit amet, consectetur adipiscing elit, sed do eiusmod tempor .</div>
</div>
<div class="card" style="left:487px;top:434px">
  <div class="photo" role="img" aria-label="Labrador lying with blue rubber toys" style="background:linear-gradient(#fff 10%,#e8cf9c 40%,#2a6fd0 70%,#fff 88%)"></div>
  <h3>Chew Rubber Toys</h3><div class="price">Price: $8.00</div>
  <div class="desc">Lorem ipsum dolor sit amet, consectetur adipiscing elit, sed do eiusmod tempor .</div>
</div>
<div class="card" style="left:56px;top:691px">
  <div class="photo" role="img" aria-label="Hamster inside a mint exercise ball" style="background:radial-gradient(circle at 50% 55%,#bfeedd 0%,#8fe0c4 45%,#fff 70%)"></div>
  <h3>Exercise Ball</h3><div class="price">Price: $18.00</div>
  <div class="desc">Lorem ipsum dolor sit amet, consectetur adipiscing elit, sed do eiusmod tempor .</div>
</div>
<div class="card" style="left:269px;top:691px">
  <div class="photo" role="img" aria-label="Green bone-shaped ID tag" style="background:radial-gradient(ellipse at 50% 55%,#7cc930 0%,#6cb92a 35%,#fff 60%)"></div>
  <h3>Personalized ID Tag</h3><div class="price">Price: $8.00</div>
  <div class="desc">Lorem ipsum dolor sit amet, consectetur adipiscing elit, sed do eiusmod tempor .</div>
</div>
<div class="card" style="left:487px;top:691px">
  <div class="photo" role="img" aria-label="Metal bird cage with two birds" style="background:radial-gradient(ellipse at 50% 55%,#d9e3e6 0%,#9fd3e6 40%,#fff 65%)"></div>
  <h3>Metal Bird Cage</h3><div class="price">Price: $8.00</div>
  <div class="desc">Lorem ipsum dolor sit amet, consectetur adipiscing elit, sed do eiusmod tempor .</div>
</div>

<footer class="abs footer">
  <div class="brand brand-footer"><span class="brand-dot"></span>SunnyPawLand</div>
  <p class="footer-about">Sed ut perspiciatis unde omnis iste natus error sit voluptatem accusantium doloremque laudantium, totam rem aperiam, eaque ipsa quae ab illo inventore veritatis et quasi architecto beatae vitae dicta sunt explicabo.</p>
  <h4 style="left:336px">Categories</h4>
  <ul style="left:336px"><li>Food &amp; Treats</li><li>Accessories</li><li>Cages &amp; Aquariums</li><li>Toys</li><li>Grooming</li></ul>
  <h4 style="left:642px">Contact</h4>
  <div class="contact">
    <div><svg width="8" height="8" viewBox="0 0 8 8"><path d="M1 0h2l1 2-1 1a5 5 0 002 2l1-1 2 1v2L7 8A7 7 0 010 1z" fill="#fff"/></svg>+49 (800) 555-0143 +49 (800) 555-0144</div>
    <div><svg width="8" height="8" viewBox="0 0 8 8"><circle cx="4" cy="4" r="3.2" fill="none" stroke="#fff" stroke-width="1.2"/><path d="M4 2v2h1.5" stroke="#fff" stroke-width="1"/></svg>7 Days a week from 9:00 am to 7:00 pm</div>
    <div><svg width="8" height="8" viewBox="0 0 8 8"><rect x=".5" y="1.5" width="7" height="5" fill="none" stroke="#fff"/><path d="M.5 1.5L4 4.5 7.5 1.5" fill="none" stroke="#fff"/></svg>hello@sunnypawland.shop</div>
  </div>
</footer>
<div class="abs bottom">
  <span class="copy">© SunnyPawLand 2017. All Rights Reserved</span>
  <div class="social"><span></span><span></span><span></span><span></span></div>
</div>
</body>
</html>
```